Workout book cover design: Looking for Simple Classic Cover

I need a book cover design for "The Steady Middle". A book on exercises to strengthen the pelvic floor. Basically it's exercises for your torso and hips. I want something tasteful and classic looking.

I like this book cover design: http://www.pagelorn-books.example/Calm-Starters-Gentle-Routines-Ease-ebook/dp/Q93KX7TM41/ref=sr_1_40?ie=UTF8&qid=2958173306&sr=8-40&keywords=exercise+books

Book Title: The Steady Middle
Description to go under title: I'm working on that now and will have ready by the end of the project. (The hidden world of pelvic floor training. Discover the best exercises for creating a strong core, hips and pelvis today!)

Target Market(s)

Mostly women 35-65 and men 60+

Industry/Entity Type

Health And Wellness

Requirements
Must have
• ebook dementions: 1536 x 2048 I think works for all the online publishing companies
• 8x10 for print
Nice to have
• I like this book cover design: http://www.pagelorn-books.example/Calm-Starters-Gentle-Routines-Ease-ebook/dp/Q93KX7TM41/ref=sr_1_40?ie=UTF8&qid=2958173306&sr=8-40&keywords=exercise+books
• This cover is also ok, but no shiny. http://www.pagelorn-books.example/Bedrock-Renew-The-Climb-Poise/dp/4827305519/ref=sr_1_2?ie=UTF8&qid=2958176642&sr=8-2&keywords=foundation+book
Should not have
• I do not like this cover, it's crowded. http://www.pagelorn-books.example/Gym-Drills-Selfweight-flexing-drills-ebook/dp/Q71RWJZNHE/ref=sr_1_2?ie=UTF8&qid=2958174418&sr=8-2&keywords=workout+books
• I do not want anyone on the cover making eye contact.

```html
<!DOCTYPE html>
<html lang="en">
<head>
<meta charset="utf-8">
<title>The Steady Middle – Cover</title>
<link rel="stylesheet" href="https://fonts.googleapis.com/css2?family=Oswald:wght@300;400;500&display=swap">
<style>
  :root {
    --backdrop: #7f6b6b;
    --sky-top: #c4def0;
    --sky-haze: #eef6fb;
    --horizon: #dfeef5;
    --sea-mid: #5f8f96;
    --sea-deep: #2e5659;
    --sea-floor: #1f3f42;
    --title-white: #ffffff;
    --title-blue: #0f9be0;
    --subtitle-blue: #1a9bdc;
    --author-white: #ffffff;
  }
  html, body {
    margin: 0;
    padding: 0;
    width: 1200px;
    height: 909px;
    overflow: hidden;
    background: var(--backdrop);
  }
  .stage {
    position: relative;
    width: 1200px;
    height: 909px;
    display: flex;
    align-items: center;
    justify-content: center;
  }
  .cover {
    position: relative;
    width: 606px;
    height: 808px;
    overflow: hidden;
    font-family: "Oswald", "Arial Narrow", sans-serif;
    text-align: center;
  }
  .cover-photo {
    position: absolute;
    inset: 0;
    background: linear-gradient(
      to bottom,
      var(--sky-top) 0%,
      var(--sky-haze) 50%,
      var(--horizon) 62%,
      var(--sea-mid) 70%,
      var(--sea-deep) 84%,
      var(--sea-floor) 100%
    );
  }
  .cover-title {
    position: absolute;
    top: 48px;
    left: 0;
    right: 0;
    margin: 0;
    font-weight: 500;
    font-size: 118px;
    line-height: 1.08;
    letter-spacing: 1px;
    text-transform: uppercase;
  }
  .cover-title .line-light { display: block; color: var(--title-white); }
  .cover-title .line-accent { display: block; color: var(--title-blue); }
  .cover-subtitle {
    position: absolute;
    top: 330px;
    left: 0;
    right: 0;
    margin: 0;
    font-weight: 300;
    font-size: 34px;
    line-height: 1.35;
    color: var(--subtitle-blue);
  }
  .cover-author {
    position: absolute;
    bottom: 38px;
    left: 0;
    right: 0;
    margin: 0;
    font-weight: 400;
    font-size: 34px;
    letter-spacing: 0.5px;
    color: var(--author-white);
    text-transform: uppercase;
  }
</style>
</head>
<body>
  <main class="stage">
    <article class="cover">
      <div class="cover-photo" role="img" aria-label="Photo of a person seen from behind, sitting cross-legged in meditation on a wet beach, facing a calm hazy sea with distant islands"></div>
      <h1 class="cover-title">
        <span class="line-light">The Steady</span>
        <span class="line-accent">Middle</span>
      </h1>
      <p class="cover-subtitle">A book on exercises to<br>strengthen the pelvic floor</p>
      <p class="cover-author">Author Name</p>
    </article>
  </main>
</body>
</html>
```